Business Card Design Project

Business card for law firm
Use existing logo
Must have:
Gerald P. Whitcombe
2715-C West 6th
McAllen, TX 78521
gwhitcombe@dvlegalgroup.com
www.dvlegalgroup.com
956-412-3095

Target Market(s)

Clients and potential clients, generally adult, business background

Industry/Entity Type

Business

Requirements
Must have
• Our logo, see below

```html
<!DOCTYPE html>
<html lang="en">
<head>
<meta charset="utf-8">
<title>Dunmore Vale – Business Card</title>
<link href="https://fonts.googleapis.com/css2?family=Cinzel:wght@400&family=Open+Sans:wght@400&display=swap" rel="stylesheet">
<style>
  :root {
    --backdrop: #e4e4e4;
    --card: #ffffff;
    --ink: #111111;
    --band-dark: #0d0d0d;
    --band-light: #2a2a2a;
    --mark: #6e6e6e;
    --tagline: #7d8c8c;
    --rule: #9a9a9a;
    --band-text: #f2f2f2;
  }
  html, body {
    margin: 0;
    width: 1200px;
    height: 985px;
    overflow: hidden;
    background: var(--backdrop);
  }
  .card {
    position: absolute;
    left: 180px;
    top: 252px;
    width: 840px;
    height: 480px;
    background: var(--card);
    border-radius: 14px;
    overflow: hidden;
    box-shadow: 0 6px 18px rgba(0,0,0,0.18);
  }
  .stripes {
    position: absolute;
    display: flex;
    flex-direction: column;
    gap: 7px;
  }
  .stripes span {
    display: block;
    height: 6px;
    background: var(--ink);
  }
  .stripes--top { left: 440px; right: 0; top: 28px; }
  .stripes--bottom { left: 0; width: 420px; top: 392px; }

  .brand {
    position: absolute;
    left: 210px;
    top: 106px;
    display: flex;
    align-items: flex-start;
    gap: 14px;
  }
  .brand__square {
    width: 62px;
    height: 62px;
    background: var(--mark);
  }
  .brand__name {
    font-family: "Cinzel", serif;
    font-weight: 400;
    font-size: 46px;
    line-height: 1;
    color: var(--ink);
    letter-spacing: 1px;
    margin: 0;
  }
  .brand__tagline {
    font-family: "Cinzel", serif;
    font-size: 19px;
    color: var(--tagline);
    margin: 4px 0 0 2px;
    padding-bottom: 6px;
    border-bottom: 1.5px solid var(--rule);
    width: 420px;
  }

  .band {
    position: absolute;
    left: 0;
    top: 200px;
    width: 745px;
    height: 172px;
    background:
      repeating-linear-gradient(135deg, rgba(255,255,255,0.035) 0 2px, transparent 2px 5px),
      linear-gradient(90deg, var(--band-dark), var(--band-light) 55%, var(--band-dark));
    color: var(--band-text);
    font-family: "Open Sans", sans-serif;
  }
  .band__person {
    position: absolute;
    left: 38px;
    top: 22px;
  }
  .person__name { font-size: 27px; margin: 0 0 4px; font-weight: 400; }
  .person__line { font-size: 20px; margin: 0; line-height: 1.3; }
  .band__divider {
    position: absolute;
    left: 345px;
    top: 40px;
    height: 100px;
    width: 1px;
    background: #6a6a6a;
  }
  .band__contacts {
    position: absolute;
    left: 368px;
    top: 46px;
    margin: 0;
    padding: 0;
    list-style: none;
  }
  .band__contacts li {
    display: flex;
    align-items: center;
    gap: 10px;
    font-size: 22px;
    line-height: 30px;
  }
  .band__contacts svg { width: 18px; height: 18px; flex: none; }
</style>
</head>
<body>
  <div class="card">
    <div class="stripes stripes--top"><span></span><span></span><span></span><span></span><span></span></div>

    <div class="brand">
      <div class="brand__square"></div>
      <div>
        <p class="brand__name">Dunmore Vale</p>
        <p class="brand__tagline">Attorneys and Counselors</p>
      </div>
    </div>

    <div class="band">
      <div class="band__person">
        <p class="person__name">Gerald P. Whitcombe</p>
        <p class="person__line">2715-C West 6th</p>
        <p class="person__line">McAllen, TX 78521</p>
      </div>
      <div class="band__divider"></div>
      <ul class="band__contacts">
        <li>
          <svg viewBox="0 0 20 20" fill="none" stroke="#f2f2f2" stroke-width="1.5"><circle cx="10" cy="10" r="8"/><ellipse cx="10" cy="10" rx="3.5" ry="8"/><line x1="2" y1="10" x2="18" y2="10"/></svg>
          gwhitcombe@dvlegalgroup.com
        </li>
        <li>
          <svg viewBox="0 0 20 20" fill="none" stroke="#f2f2f2" stroke-width="1.5"><rect x="2" y="4" width="16" height="12"/><polyline points="2,4 10,11 18,4"/></svg>
          www.dvlegalgroup.com
        </li>
        <li>
          <svg viewBox="0 0 20 20"><rect x="1" y="1" width="18" height="18" rx="3" fill="#f2f2f2"/><path d="M7 5c-1.5 1-1.5 3 0 6s3.5 4.5 5 4l1-2-2-1-1 1c-1-.5-2-2-2.5-3l1-1-1-2z" fill="#111"/></svg>
          956-412-3095
        </li>
      </ul>
    </div>

    <div class="stripes stripes--bottom"><span></span><span></span><span></span><span></span><span></span></div>
  </div>
</body>
</html>
```